Geschäftspapiere für Jobwebseite
Zielgruppe
Hier finden sie alle Informationen zu unserem Unternehmen:
https://www.heller-wandel.com
Aufgabenstellung
Gerne von den Farben angelehnt an die Website ein modernes Briefpapier gestalten.

```html
<!DOCTYPE html>
<html lang="de">
<head>
<meta charset="utf-8">
<title>Heller-Wandel Geschäftspapiere</title>
<link rel="stylesheet" href="https://fonts.googleapis.com/css2?family=Open+Sans:wght@700&family=Quicksand:wght@300;400&display=swap">
<style>
:root{
  --stage:#4b4b4b;
  --paper:#ffffff;
  --green:#2eaa4f;
  --ink:#3f4350;
  --wordmark:#333333;
  --faint-green:#eef7ef;
  --faint-grey:#e8e8ea;
  --shadow:0 6px 10px rgba(0,0,0,.45);
}
*{margin:0;padding:0;box-sizing:border-box}
html,body{width:1200px;height:1200px;overflow:hidden;background:var(--stage)}
body{position:relative;font-family:'Quicksand',sans-serif}
.sheet{position:absolute;background:var(--paper);box-shadow:var(--shadow);overflow:hidden}
.top-bar{position:absolute;left:0;top:0;width:100%;height:9px;background:var(--green)}
.wordmark{position:absolute;font-family:'Open Sans',sans-serif;font-weight:700;color:var(--wordmark);white-space:nowrap;letter-spacing:.2px}
.mark{position:absolute;border-radius:50%;background:var(--green)}
.stripe{position:absolute;height:9px}
.stripe.dark{background:var(--ink)}
.stripe.green{background:var(--green)}
.contact{position:absolute;color:var(--green);font-weight:300;white-space:nowrap}

/* letterhead */
.letterhead{left:31px;top:88px;width:504px;height:712px}
.letterhead .wordmark{left:25px;top:30px;font-size:19px}
.letterhead .contact{left:384px;top:27px;font-size:7.5px;line-height:15.6px}
.letterhead .watermark{position:absolute;left:160px;top:260px;width:170px;height:170px;border-radius:50%;background:var(--faint-green)}
.fold{position:absolute;left:0;width:18px;height:1px;background:#ddd}
.letterhead .footer{position:absolute;left:45px;top:690px;font-size:6.2px;color:var(--green);white-space:nowrap}

/* envelope back */
.envelope-back{left:586px;top:100px;width:557px;height:279px}
.flap{position:absolute;left:0;top:0;width:557px;height:79px}
.flap-text{position:absolute;left:0;top:53px;width:100%;text-align:center;color:#fff;font-size:10px;font-weight:300}
.flap-mark{position:absolute;left:268px;top:14px;width:22px;height:22px;border-radius:50%;background:rgba(255,255,255,.45)}

/* envelope front */
.envelope-front{left:597px;top:521px;width:557px;height:279px}
.envelope-front .wordmark{left:27px;top:30px;font-size:19px}

/* business cards */
.card{top:848px;width:390px;height:251px}
.card-front{left:230px}
.card-back{left:633px}
.card-front .person{position:absolute;left:22px;top:26px;font-size:10px;line-height:11px;color:var(--ink);font-weight:400}
.card-front .person .role{color:var(--green);font-weight:300}
.card-front .contact{left:22px;font-size:9.6px;line-height:15.6px}
.card-front .big-mark{position:absolute;left:245px;top:45px;width:110px;height:110px;border-radius:50%;background:var(--green)}
.card-front .wordmark{left:226px;top:190px;font-size:14px}
.card-back .wordmark{left:0;width:100%;text-align:center;top:86px;font-size:26px}
</style>
</head>
<body>

<section class="sheet letterhead">
  <div class="top-bar"></div>
  <div class="wordmark">HELLER-WANDEL.de</div>
  <div class="contact">Kontakt<br>Gewerbering Nord 7<br>76133 Karlsruhe<br>E-Mail: info@heller-wandel.de<br>Telefon:&nbsp; 0721 555 018 3</div>
  <div class="fold" style="top:252px"></div>
  <div class="fold" style="top:491px"></div>
  <div class="watermark" role="img" aria-label="Dezentes Markenzeichen als Hintergrund"></div>
  <div class="stripe dark" style="left:0;top:671px;width:402px"></div>
  <div class="mark" style="left:410px;top:660px;width:22px;height:22px"></div>
  <div class="stripe green" style="left:436px;top:671px;width:68px"></div>
  <div class="footer">Bankverbindung: Musterbank DE00000111000010186012 MUBAXXXXXXX &nbsp;•&nbsp; Steuernummer 000/000/00000</div>
</section>

<section class="sheet envelope-back">
  <svg class="flap" viewBox="0 0 557 79" aria-hidden="true">
    <path d="M0 0 H557 L532 72 Q530 79 522 79 H35 Q27 79 25 72 Z" fill="var(--green)"/>
  </svg>
  <div class="flap-mark"></div>
  <div class="flap-text">Gewerbering Nord 7 &nbsp;&nbsp;●&nbsp; 76133 Karlsruhe</div>
</section>

<section class="sheet envelope-front">
  <div class="wordmark">HELLER-WANDEL.de</div>
  <div class="stripe dark" style="left:0;top:238px;width:456px"></div>
  <div class="mark" style="left:462px;top:227px;width:22px;height:22px"></div>
  <div class="stripe green" style="left:489px;top:238px;width:68px"></div>
</section>

<section class="sheet card card-front">
  <div class="top-bar"></div>
  <div class="person">Herr Jonas Brenner<br><span class="role">Inhaber</span></div>
  <div class="contact" style="top:54px">E-Mail: jonas.brenner@heller-wandel.de<br>Telefon: 0721 555 018 3</div>
  <div class="contact" style="top:105px">Kontakt<br>Gewerbering Nord 7<br>76133 Karlsruhe<br>E-Mail: info@heller-wandel.de<br>Telefon:&nbsp; 0721 555 018 3</div>
  <div class="big-mark"></div>
  <div class="wordmark">HELLER-WANDEL.de</div>
  <div class="stripe green" style="left:0;top:218px;width:70px"></div>
  <div class="mark" style="left:76px;top:207px;width:22px;height:22px"></div>
  <div class="stripe dark" style="left:101px;top:218px;width:289px"></div>
</section>

<section class="sheet card card-back">
  <div class="wordmark">HELLER-WANDEL.de</div>
  <div class="stripe dark" style="left:0;top:218px;width:288px"></div>
  <div class="mark" style="left:294px;top:207px;width:22px;height:22px"></div>
  <div class="stripe green" style="left:320px;top:218px;width:70px"></div>
</section>

</body>
</html>
```